Business Card Design

We need a business card design for a new company located in Missouri City, TX, entitled 'BrightPath Chiropractic & Holistic Center'. Our services include restoration of health and vitality, spinal exam, health assessment, dietary & fitness programs, lymphatic & therapeutic massage, detox & remineralize body wraps, far infrared sauna therapy

Industry/Entity Type

Business

Contact Information for Business Card

BrightPath Chiropractic & Holistic Center, Marlene Voskit LMT, 4215 Hwy. 9, Suite 310, Missouri City, TX 77512, 281-634-9057

```html
<!DOCTYPE html>
<html lang="en">
<head>
<meta charset="utf-8">
<title>BrightPath Chiropractic &amp; Holistic Center – Business Card</title>
<link rel="stylesheet" href="https://fonts.googleapis.com/css2?family=Didact+Gothic&display=swap">
<style>
  :root {
    --brand-green: #1a7f69;
    --brand-green-dark: #135c4c;
    --glow-green: #4fd0a6;
    --paper: #ffffff;
    --ink-light: #ffffff;
  }
  html, body {
    margin: 0;
    padding: 0;
    width: 1200px;
    height: 680px;
    overflow: hidden;
    background: var(--paper);
  }
  .card {
    position: relative;
    width: 1200px;
    height: 680px;
    overflow: hidden;
    background: var(--paper);
    font-family: "Didact Gothic", "Questrial", sans-serif;
  }
  .card-background {
    position: absolute;
    inset: 0;
    width: 1200px;
    height: 680px;
  }
  .brand-name {
    position: absolute;
    left: 62px;
    top: 40px;
    margin: 0;
    color: var(--brand-green);
    font-weight: 400;
    text-transform: uppercase;
    line-height: 1;
  }
  .brand-name-line1 {
    display: block;
    font-size: 56px;
    letter-spacing: 0.5px;
  }
  .brand-name-line2 {
    display: block;
    margin-top: 14px;
    font-size: 78px;
    letter-spacing: 1px;
  }
  .brand-mark {
    position: absolute;
    left: 1042px;
    top: 86px;
    width: 64px;
    height: 64px;
    background: var(--brand-green);
  }
  .contact {
    position: absolute;
    right: 135px;
    color: var(--ink-light);
    text-align: right;
    text-transform: uppercase;
    line-height: 1;
    margin: 0;
  }
  .contact-phone {
    top: 404px;
    font-size: 33px;
  }
  .contact-address {
    top: 482px;
    font-size: 25px;
    line-height: 36px;
  }
  .contact-web {
    top: 588px;
    font-size: 35px;
  }
  .contact-icon {
    position: absolute;
    fill: var(--ink-light);
  }
  .icon-phone { left: 1082px; top: 402px; width: 48px; height: 40px; }
  .icon-pin { left: 1090px; top: 488px; width: 32px; height: 48px; }
  .icon-globe { left: 1085px; top: 587px; width: 42px; height: 42px; }
</style>
</head>
<body>
<div class="card">
  <svg class="card-background" viewBox="0 0 1063 602" preserveAspectRatio="none" aria-hidden="true">
    <defs>
      <linearGradient id="band-shade" x1="0" y1="0" x2="1" y2="0">
        <stop offset="0" stop-color="#0a0a0a"/>
        <stop offset="0.2" stop-color="#2a2a2a"/>
        <stop offset="0.48" stop-color="#ffffff"/>
        <stop offset="0.7" stop-color="#e6e6e6"/>
        <stop offset="0.88" stop-color="#6f7c79"/>
        <stop offset="1" stop-color="#05201a"/>
      </linearGradient>
      <linearGradient id="field-shade" x1="0" y1="0" x2="0.3" y2="1">
        <stop offset="0" stop-color="#1b846d"/>
        <stop offset="1" stop-color="#145f4f"/>
      </linearGradient>
      <radialGradient id="green-glow" cx="0.5" cy="0.5" r="0.5">
        <stop offset="0" stop-color="#45c99c" stop-opacity="0.95"/>
        <stop offset="0.4" stop-color="#8fe0c3" stop-opacity="0.45"/>
        <stop offset="1" stop-color="#ffffff" stop-opacity="0"/>
      </radialGradient>
      <radialGradient id="white-glow" cx="0.5" cy="0.5" r="0.5">
        <stop offset="0" stop-color="#ffffff" stop-opacity="0.9"/>
        <stop offset="0.45" stop-color="#ffffff" stop-opacity="0.35"/>
        <stop offset="1" stop-color="#ffffff" stop-opacity="0"/>
      </radialGradient>
    </defs>
    <path class="green-field" d="M0,432 Q560,318 1063,205 V602 H0 Z" fill="url(#field-shade)"/>
    <ellipse cx="495" cy="272" rx="150" ry="110" fill="url(#green-glow)"/>
    <path class="swoosh-band" d="M0,378 Q560,262 1063,163 L1063,205 Q560,318 0,432 Z" fill="url(#band-shade)"/>
    <ellipse cx="540" cy="345" rx="130" ry="90" fill="url(#white-glow)"/>
  </svg>

  <h1 class="brand-name">
    <span class="brand-name-line1">BrightPath Chiropractic</span>
    <span class="brand-name-line2">&amp; Holistic Center</span>
  </h1>
  <div class="brand-mark" aria-hidden="true"></div>

  <p class="contact contact-phone">281-634-9057</p>
  <svg class="contact-icon icon-phone" viewBox="0 0 48 40" aria-hidden="true">
    <path d="M4,14 C4,6 44,6 44,14 L44,18 L34,18 L34,13 C28,11 20,11 14,13 L14,18 L4,18 Z"/>
    <path d="M12,20 L18,16 L30,16 L36,20 L40,36 L8,36 Z"/>
    <circle cx="24" cy="27" r="6" fill="#1a7f69"/>
    <circle cx="24" cy="27" r="2.5"/>
  </svg>

  <p class="contact contact-address">Marlene Voskit LMT, 4215 Hwy. 9<br>Suite 310, Missouri City, TX 77512</p>
  <svg class="contact-icon icon-pin" viewBox="0 0 32 48" aria-hidden="true">
    <path d="M16,0 C7,0 0,7 0,16 C0,28 16,48 16,48 C16,48 32,28 32,16 C32,7 25,0 16,0 Z M16,22 A6,6 0 1 1 16,10 A6,6 0 1 1 16,22 Z"/>
  </svg>

  <p class="contact contact-web">www.brightpathchirocenter.com</p>
  <svg class="contact-icon icon-globe" viewBox="0 0 42 42" aria-hidden="true">
    <g fill="none" stroke="#ffffff" stroke-width="3">
      <circle cx="21" cy="21" r="18"/>
      <ellipse cx="21" cy="21" rx="8" ry="18"/>
      <line x1="21" y1="3" x2="21" y2="39"/>
      <line x1="3" y1="21" x2="39" y2="21"/>
      <path d="M6,12 H36 M6,30 H36"/>
    </g>
  </svg>
</div>
</body>
</html>
```